Business cards and stationary for IT Service Provider
Vantry Datacraft
Business cards and stationary for IT Service Provider - Information Technology
Creative Brief
Use specific fonts
No preference, we have used is called ETHNOCENTRIC for the tagline
Bright & Fun-filled
Peter Hollins
Director
Meadowbank Upper Fenwick Lane Brindlow, Preston PR5 7QT
pete@orlendatacraft-mail.com
www.orlendatacraft-mail.com
VAT Number and company registration number to be included somewhere on business card. VAT Number: 846 227 51 Company Registration Number: 4918264 In addition to letterhead we would also like a continuation sheet.
All the information we require is listed above, everything else is entirely up to you!
orlendatacraft orlendatacraft
Please note that this project is for Business Cards AND Stationary. Could we see some Letterheads too?

```html
<!DOCTYPE html>
<html lang="en">
<head>
<meta charset="utf-8">
<title>Vantry Datacraft – Business Cards</title>
<link href="https://fonts.googleapis.com/css2?family=Orbitron:wght@500;700&family=Questrial&display=swap" rel="stylesheet">
<style>
  :root{
    --stage:#4b4b4b;
    --teal:#2db3a6;
    --charcoal:#3a3a3c;
    --ink:#2b2b2d;
    --paper:#ffffff;
  }
  *{margin:0;padding:0;box-sizing:border-box}
  html,body{width:1200px;height:895px;overflow:hidden;background:var(--stage)}
  .canvas{position:relative;width:1200px;height:895px}
  .card{position:absolute;background:var(--paper);overflow:hidden}
  .card-shapes{position:absolute;inset:0}
  .card-front{left:110px;top:110px;width:560px;height:320px}
  .card-back{left:500px;top:450px;width:600px;height:340px}

  .wordmark{position:absolute;font-family:'Orbitron',sans-serif;font-weight:700;color:var(--teal);letter-spacing:1px;white-space:nowrap}
  .card-front .wordmark{left:28px;top:146px;font-size:19px}
  .card-back .wordmark{left:0;right:0;top:88px;text-align:center;font-size:34px;letter-spacing:2px}

  .contact{position:absolute;right:20px;top:34px;width:270px;text-align:right;font-family:'Questrial',sans-serif;color:var(--ink)}
  .contact .person{font-family:'Orbitron',sans-serif;font-weight:500;font-size:14px;letter-spacing:1.5px}
  .contact .role{font-size:11px;margin-top:3px}
  .contact .address{font-size:10.5px;line-height:1.45;margin-top:30px;margin-left:70px}
  .contact .lines{list-style:none;margin-top:22px}
  .contact .lines li{display:flex;justify-content:flex-end;align-items:center;gap:8px;font-size:10px;height:16px}
  .contact .lines li:nth-child(4){margin-top:6px}
  .contact svg{width:10px;height:10px;fill:var(--ink)}

  .website{position:absolute;left:0;right:0;bottom:22px;text-align:center;font-family:'Orbitron',sans-serif;font-weight:500;font-size:15px;letter-spacing:5px;color:var(--ink)}
</style>
</head>
<body>
<main class="canvas">

  <section class="card card-front" aria-label="Business card, contact side">
    <svg class="card-shapes" viewBox="0 0 560 320" preserveAspectRatio="none" aria-hidden="true">
      <path d="M238,0 Q326,160 238,320 L560,320 L560,0 Z" fill="var(--charcoal)"/>
      <path d="M250,0 Q338,160 250,320 L560,320 L560,0 Z" fill="var(--teal)"/>
    </svg>
    <div class="wordmark">Vantry Datacraft</div>
    <div class="contact">
      <div class="person">PETER HOLLINS</div>
      <div class="role">Director</div>
      <div class="address">Meadowbank Upper Fenwick Lane<br>Brindlow, Preston PR5 7QT</div>
      <ul class="lines">
        <li>VAT 846 227 51<svg viewBox="0 0 10 10"><path d="M2 0.5l2 2-1 1.2c.6 1.3 1.6 2.3 2.9 2.9l1.2-1 2 2-1.3 1.6C4.6 9 1 5.4.4 1.8z"/></svg></li>
        <li>Reg 4918264<svg viewBox="0 0 10 10"><path d="M2.5 0h5v10h-5zM3.5 1v7h3V1z"/></svg></li>
        <li>012 345 6789<svg viewBox="0 0 10 10"><path d="M2 0h6v3H2zM0 3.5h10V8H8v2H2V8H0zM3 6.5v2.5h4V6.5z"/></svg></li>
        <li>pete@vantrydatacraft-mail.com<svg viewBox="0 0 10 10"><path d="M0 2h10v6H0zM1 3v.4l4 2.6 4-2.6V3z"/></svg></li>
        <li>www.vantrydatacraft-mail.com<svg viewBox="0 0 10 10"><path d="M5 0a5 5 0 1 0 0 10A5 5 0 0 0 5 0zm0 1.2a3.8 3.8 0 1 1 0 7.6 3.8 3.8 0 0 1 0-7.6zM1.5 4.5h7v1h-7z"/></svg></li>
      </ul>
    </div>
  </section>

  <section class="card card-back" aria-label="Business card, brand side">
    <svg class="card-shapes" viewBox="0 0 600 340" preserveAspectRatio="none" aria-hidden="true">
      <path d="M0,188 Q360,176 600,276 L600,340 L0,340 Z" fill="var(--charcoal)"/>
      <path d="M0,200 Q360,190 600,290 L600,340 L0,340 Z" fill="var(--teal)"/>
    </svg>
    <div class="wordmark">Vantry Datacraft</div>
    <div class="website">www.vantrydatacraft-mail.com</div>
  </section>

</main>
</body>
</html>
```